I need a logo design for a new company based in Tucson called "Mindpilot Reg Holloway". I am a psychotherapist that specializes in clinical psychology with athletes and performers. The final design should incorporate the psychology symbol as a watermark. The logo should convey movement and fluidity. "Mindpilot" is a bit of a play on words combining psychology (head) with sports (coach). Other design interests include mid-century, Ansel Brigham Kotter. I will want to use the logo for business cards, letterhead and marketing brochures. I will put together a website at a later date. I am attaching a file with some pertinent information for the business card. Thank you.
Reg Holloway
mindpilotregholloway@quillmarsh.net
Updates

Thank you all for the submissions so far.  I have submitted an additional file with a draft of a new design idea.  Since "mindpilot" is a bit of a play on words, I would like to see something with the two "H's" look something like quotation marks.  If the psychology logo is to be included at all, it needs to be less prominent.     Thank you all.  Reg                               

Target Market(s)

1) Adolescent and adult athletes and performers who are looking to increase their level of performance (Sport and Performance Psychology)
2) Adult psychotherapy patients (Clinical psychology)

Industry/Entity Type

Marketing

Colors

Designer to choose colors to be used in the design.

Requirements
Must have
• 1) Since "mindpilot" is a bit of a play on words, The "H's" need to be in a font that looks somewhat like quotation marks.

Nice to have
• Logo on one side. All other info on the backside?

```html
<!DOCTYPE html>
<html lang="en">
<head>
<meta charset="utf-8">
<title>Mind Pilot – Business Card</title>
<link href="https://fonts.googleapis.com/css2?family=Montserrat:wght@300;400;700&display=swap" rel="stylesheet">
<style>
  :root {
    --bg: #e6e6e4;
    --card-dark: #0d0d0d;
    --card-light: #ffffff;
    --brand-green: #3fbf5a;
    --watermark-green: #b9e8c5;
    --text-light: #ffffff;
    --text-muted: #d6d6d6;
  }
  * { margin: 0; padding: 0; box-sizing: border-box; }
  html, body {
    width: 1200px; height: 873px; overflow: hidden;
    background: var(--bg);
  }
  .business-card {
    position: absolute; left: 75px; top: 136px;
    width: 1050px; height: 600px;
    display: flex; overflow: hidden;
    box-shadow: 0 10px 30px rgba(0,0,0,.18);
    font-family: "Montserrat", sans-serif;
  }
  .card-front {
    position: relative; width: 600px; height: 100%;
    background: var(--card-dark); color: var(--text-light);
  }
  .wordmark {
    position: absolute; left: 60px; top: 48px;
    font-weight: 700; color: var(--brand-green);
    font-size: 92px; line-height: 96px; letter-spacing: 1px;
  }
  .wordmark span { display: block; }
  .wordmark .line-one { padding-left: 90px; }
  .contact-name {
    position: absolute; left: 60px; top: 292px;
    font-weight: 700; font-size: 30px;
  }
  .contact-title {
    position: absolute; left: 60px; top: 334px;
    font-weight: 300; font-size: 27px; color: var(--text-muted);
  }
  .divider {
    position: absolute; left: 60px; top: 388px;
    width: 470px; height: 4px; background: var(--text-light);
  }
  .divider::before {
    content: ""; position: absolute; left: 0; top: 0;
    width: 70px; height: 100%; background: var(--brand-green);
  }
  .specialty {
    position: absolute; left: 60px; top: 414px;
    font-weight: 700; font-size: 19px;
  }
  .contact-list {
    position: absolute; left: 60px; top: 452px;
    list-style: none; font-size: 17px; font-weight: 400;
  }
  .contact-list li {
    display: flex; align-items: center; gap: 14px; height: 36px;
  }
  .contact-icon { width: 24px; height: 24px; flex: none; }
  .card-back {
    position: relative; flex: 1; height: 100%;
    background: var(--card-light); overflow: hidden;
  }
  .watermark-word {
    position: absolute; top: 30px;
    writing-mode: vertical-rl;
    font-weight: 700; color: var(--watermark-green);
    font-size: 130px; line-height: 1; letter-spacing: 4px;
    white-space: nowrap;
  }
  .watermark-word.first { left: 70px; }
  .watermark-word.second { left: 245px; }
</style>
</head>
<body>
  <div class="business-card">
    <section class="card-front">
      <div class="wordmark" aria-label="Mind Pilot">
        <span class="line-one">MIND</span>
        <span class="line-two">PILOT</span>
      </div>
      <p class="contact-name">Reg H. Holloway MA</p>
      <p class="contact-title">Licensed Professional Counselor</p>
      <div class="divider"></div>
      <p class="specialty">Clinical &amp; Athletic Performance Psychology</p>
      <ul class="contact-list">
        <li>
          <svg class="contact-icon" viewBox="0 0 24 24" aria-hidden="true">
            <rect width="24" height="24" fill="var(--brand-green)"/>
            <path d="M12 5a4.5 4.5 0 0 0-4.5 4.5c0 3.4 4.5 9 4.5 9s4.5-5.6 4.5-9A4.5 4.5 0 0 0 12 5z" fill="#fff"/>
            <circle cx="12" cy="9.5" r="1.7" fill="var(--brand-green)"/>
          </svg>
          4417 North Calder Ave #210 Tucson, AZ 85719
        </li>
        <li>
          <svg class="contact-icon" viewBox="0 0 24 24" aria-hidden="true">
            <rect width="24" height="24" fill="var(--brand-green)"/>
            <path d="M8 5h3l1.2 3.5-1.8 1.3a8 8 0 0 0 3.8 3.8l1.3-1.8L19 13v3a2 2 0 0 1-2 2A12 12 0 0 1 6 7a2 2 0 0 1 2-2z" fill="#fff"/>
          </svg>
          520.555.0187 (mobile)&nbsp; 520.555.0142 (fax)
        </li>
        <li>
          <svg class="contact-icon" viewBox="0 0 24 24" aria-hidden="true">
            <rect width="24" height="24" fill="var(--brand-green)"/>
            <rect x="5" y="7" width="14" height="10" fill="#fff"/>
            <path d="M5 7l7 5.5L19 7" fill="none" stroke="var(--brand-green)" stroke-width="1.5"/>
          </svg>
          mindpilotregholloway@quillmarsh.net
        </li>
      </ul>
    </section>
    <section class="card-back" aria-label="Mind Pilot watermark">
      <span class="watermark-word first">MIND</span>
      <span class="watermark-word second">PILOT</span>
    </section>
  </div>
</body>
</html>
```